Bluetooth Earphone Packaging Design

We want to use the packaging for 4-5 of our Bluetooth Earphone series (Picture enclosed) and hence we would not like to put any product pictures on the packaging.

Material: E-Flute Paper box
Type: Window Box style
Design features we prefer: Colorful, creative, trendy, High tech.
Requirement: AI file is preferred
Size of Packaging: (L) 95 x (W) 40 x (H) 120 mm

Enclosed are a detailed description along with competitor designs for your reference.

Any further questions, please feel free to ask

```html
<!DOCTYPE html>
<html lang="en">
<head>
<meta charset="utf-8">
<title>Earphone Packaging – Front and Back Panels</title>
<link href="https://fonts.googleapis.com/css2?family=League+Spartan:wght@500;600;700&family=Roboto:ital,wght@1,400&display=swap" rel="stylesheet">
<style>
  :root {
    --backdrop: #b3b3b2;
    --panel: #edeef0;
    --side: #cfd0d2;
    --side-band: #38383a;
    --ink: #3e3e40;
    --sky: #6ccaf2;
    --band: #4b4b4d;
    --band-text: #e9eaec;
    --rule: #a9aaad;
    --slot: #1c1c1c;
    --note: #c9cacc;
    --label: #1f1f1f;
    --frame: #2a2a2a;
  }
  * { margin: 0; padding: 0; box-sizing: border-box; }
  html, body { width: 1200px; height: 1198px; overflow: hidden; }
  body {
    background: var(--backdrop);
    font-family: "League Spartan", "Helvetica Neue", sans-serif;
    position: relative;
  }
  .box { position: absolute; top: 314px; height: 648px; }
  .box--front { left: 117px; width: 461px; }
  .box--back { left: 653px; width: 462px; }
  .side {
    position: absolute; left: 0; top: 6px; bottom: 0; width: 36px; background: var(--side);
  }
  .side::after {
    content: ""; position: absolute; left: 0; right: 0; bottom: 0; height: 64px; background: var(--side-band);
  }
  .face {
    position: absolute; left: 36px; top: 0; right: 0; bottom: 0; background: var(--panel);
    box-shadow: 8px 8px 10px rgba(0,0,0,.25);
  }
  .hang-tab {
    position: absolute; top: -70px; left: 50%; transform: translateX(-50%);
    width: 162px; height: 72px; background: #fff; border-radius: 16px 16px 0 0;
  }
  .hang-tab__slot {
    position: absolute; left: 38px; top: 30px; width: 86px; height: 15px;
    background: var(--slot); border-radius: 8px;
  }
  .hang-tab__slot::before {
    content: ""; position: absolute; left: 31px; top: -9px; width: 24px; height: 15px;
    background: var(--slot); border-radius: 12px 12px 0 0;
  }
  .band {
    position: absolute; left: 0; right: 0; bottom: 0; height: 64px; background: var(--band);
    display: flex; align-items: center; gap: 7px; padding-left: 24px;
  }
  .band__dot { width: 16px; height: 16px; border-radius: 50%; background: var(--band-text); }
  .band__name { color: var(--band-text); font-weight: 600; font-size: 24px; letter-spacing: .3px; }
  .title { position: absolute; font-weight: 700; line-height: .9; letter-spacing: -.5px; }
  .title__line--dark { color: var(--ink); display: block; }
  .title__line--blue { color: var(--sky); display: block; }
  .box--front .title { left: 15px; top: 22px; font-size: 60px; }
  .box--back .title { left: 15px; top: 32px; font-size: 30px; }
  .window { position: absolute; left: 52px; top: 159px; }
  .features { position: absolute; left: 36px; top: 436px; color: var(--ink); }
  .features__head { font-weight: 600; font-size: 22px; margin-bottom: 5px; }
  .features__list { list-style: none; font-weight: 600; font-size: 14px; line-height: 1.2; }
  .features__list li::before { content: "· "; }
  .note { position: absolute; background: var(--note); border-radius: 10px; }
  .specs { position: absolute; left: 50px; top: 140px; width: 260px; list-style: none; }
  .specs li {
    color: var(--sky); font-weight: 600; font-size: 14px; height: 34px;
    padding-top: 9px; border-bottom: 1.5px solid var(--rule);
  }
  .specs li:last-child { border-bottom: none; }
  .barcode-frame {
    position: absolute; left: 298px; top: 467px; width: 103px; height: 86px;
    border: 1.5px solid var(--frame);
  }
  .annotation {
    position: absolute; font-family: "Roboto", Arial, sans-serif; font-style: italic;
    font-size: 15px; color: var(--label); white-space: nowrap;
  }
  .dims { position: absolute; left: 0; top: 0; }
</style>
</head>
<body>
  <svg class="dims" width="1200" height="1198" aria-hidden="true">
    <g stroke="#222" stroke-width="1.2" fill="none">
      <line x1="86" y1="316" x2="96" y2="912"/>
      <polyline points="81,324 86,316 91,324"/>
      <polyline points="91,904 96,912 101,904"/>
      <line x1="112" y1="928" x2="152" y2="982"/>
      <polyline points="112,937 112,928 121,931"/>
      <polyline points="143,979 152,982 152,973"/>
      <line x1="168" y1="997" x2="574" y2="958"/>
      <polyline points="177,992 168,997 178,1001"/>
      <polyline points="564,955 574,958 566,965"/>
      <line x1="592" y1="642" x2="640" y2="680"/>
      <polyline points="592,651 592,642 601,643"/>
      <line x1="1122" y1="864" x2="1162" y2="908"/>
      <polyline points="1122,873 1122,864 1131,866"/>
      <line x1="912" y1="970" x2="947" y2="1018"/>
      <polyline points="912,979 912,970 921,973"/>
    </g>
  </svg>
  <span class="annotation" style="left:30px;top:587px;">120mm</span>
  <span class="annotation" style="left:64px;top:965px;">40mm</span>
  <span class="annotation" style="left:372px;top:987px;">95mm</span>
  <span class="annotation" style="left:592px;top:697px;">WINDOW</span>
  <span class="annotation" style="left:1123px;top:914px;">BARCODE</span>
  <span class="annotation" style="left:917px;top:1035px;">MANUFACTURER INFO</span>

  <section class="box box--front">
    <div class="side"></div>
    <div class="face">
      <div class="hang-tab"><span class="hang-tab__slot"></span></div>
      <h1 class="title">
        <span class="title__line--dark">BLUETOOTH</span>
        <span class="title__line--blue">EARPHONE 5.0</span>
      </h1>
      <svg class="window" width="325" height="265" role="img" aria-label="Die-cut window showing the white earphones inside">
        <defs>
          <linearGradient id="windowShade" x1="0" y1="0" x2="0" y2="1">
            <stop offset="0" stop-color="#a9aaad"/>
            <stop offset="1" stop-color="#e4e5e7"/>
          </linearGradient>
        </defs>
        <polygon points="2,10 322,2 172,262" fill="url(#windowShade)" stroke="#7d7e81" stroke-width="2"/>
      </svg>
      <div class="features">
        <p class="features__head">FEATURES</p>
        <ul class="features__list">
          <li>BLUETOOTH 5.0</li>
          <li>EXCEPTIONAL SOUND QUALITY</li>
          <li>HIGH DEFINITION MICROPHONE</li>
        </ul>
      </div>
      <div class="note" role="img" aria-label="Music note sketch" style="left:334px;top:426px;width:57px;height:67px;"></div>
      <div class="note" role="img" aria-label="Music note sketch" style="left:256px;top:507px;width:66px;height:50px;"></div>
      <div class="band"><span class="band__dot"></span><span class="band__name">Wavelink</span></div>
    </div>
  </section>

  <section class="box box--back">
    <div class="side"></div>
    <div class="face">
      <div class="hang-tab"><span class="hang-tab__slot"></span></div>
      <h2 class="title">
        <span class="title__line--dark">BLUETOOTH</span>
        <span class="title__line--blue">EARPHONE 5.0</span>
      </h2>
      <div class="note" role="img" aria-label="Music note sketch" style="left:253px;top:35px;width:67px;height:48px;"></div>
      <div class="note" role="img" aria-label="Music note sketch" style="left:337px;top:66px;width:62px;height:67px;"></div>
      <ul class="specs">
        <li>BLUETOOTH VERSION: 5.0</li>
        <li>WIRELESS PLAYBACK DURATION: 3-4 H</li>
        <li>STANDBY TIME: 80 H</li>
        <li>WIRELESS RANGE: 10 M</li>
        <li>IMPEDANCE: 32 Ω</li>
        <li>SOUND PRESSURE LEVEL: 100DB ± 3DB</li>
        <li>FREQUENCY RESPONSE: 20-20KHZ</li>
        <li>DRIVER UNIT: 10MM</li>
      </ul>
      <div class="barcode-frame" aria-label="Barcode area"></div>
      <div class="band"><span class="band__dot"></span><span class="band__name">Wavelink</span></div>
    </div>
  </section>
</body>
</html>
```